Association Insurance WhitePaper

Need white paper layout design for cover page, data pages and back page, much like a powerpoint design. Looking for similar designs as the uploaded drawing style.

```html
<!DOCTYPE html>
<html lang="en">
<head>
<meta charset="utf-8">
<title>Harwick Association Insurance – White Paper</title>
<link href="https://fonts.googleapis.com/css2?family=Poppins:wght@400;500;600;700;800;900&display=swap" rel="stylesheet">
<style>
  :root {
    --stage: #2d2b2b;
    --paper: #ffffff;
    --ink: #0b0b0b;
    --text: #3a3a3a;
    --orange: #f26522;
    --deep-red: #b3261e;
    --grid: #d9dde2;
    --blue: #2a9fd6;
    --pink: #e6197d;
  }
  * { margin: 0; padding: 0; box-sizing: border-box; }
  html, body { width: 964px; height: 1200px; overflow: hidden; }
  body { background: var(--stage); font-family: "Poppins", sans-serif; position: relative; }

  .page { position: absolute; width: 409px; height: 528px; background: var(--paper); overflow: hidden; }
  .page--cover { left: 59px; top: 54px; }
  .page--data { left: 497px; top: 54px; }
  .page--back { left: 497px; top: 619px; }

  /* Cover */
  .cover-frame { position: absolute; left: 24px; right: 24px; top: 13px; height: 378px; border: 1px solid var(--orange); }
  .cover-tagline { position: absolute; top: 36px; left: 0; right: 0; text-align: center; font-size: 5.6px; font-weight: 700; color: var(--deep-red); letter-spacing: 0.02em; }
  .cover-title { position: absolute; top: 46px; left: 0; right: 0; text-align: center; font-size: 38px; font-weight: 900; line-height: 43px; color: var(--ink); letter-spacing: 0.01em; }
  .cover-lead { position: absolute; top: 180px; left: 40px; right: 40px; text-align: center; font-size: 11px; font-weight: 600; line-height: 19px; color: var(--orange); }
  .cover-body { position: absolute; top: 226px; left: 50px; right: 50px; text-align: center; font-size: 7px; line-height: 16px; color: var(--text); }
  .date-pill { position: absolute; top: 285px; left: 165px; width: 77px; height: 19px; border-radius: 10px; background: var(--orange); color: #fff; font-size: 7.3px; font-weight: 600; display: flex; align-items: center; justify-content: center; gap: 4px; }
  .cover-art { position: absolute; left: 0; right: 0; top: 302px; bottom: 0;
    background: radial-gradient(ellipse at 30% 20%, rgba(150,175,200,0.55), transparent 55%),
                linear-gradient(180deg, rgba(255,255,255,0) 0%, #d98a5e 35%, #b8553a 60%, #8a5a4a 85%, #e8e2da 100%); }

  /* Data page */
  .data-title { position: absolute; left: 33px; top: 20px; font-size: 23.5px; font-weight: 800; line-height: 29px; color: var(--ink); letter-spacing: 0.01em; }
  .side-band { position: absolute; left: 0; top: 95px; width: 52px; bottom: 0; background: var(--orange); }
  .data-kicker { position: absolute; left: 77px; width: 300px; top: 97px; font-size: 7.4px; font-weight: 700; line-height: 14px; color: var(--orange); }
  .data-body { position: absolute; left: 77px; width: 296px; top: 129px; font-size: 6.7px; line-height: 14.1px; color: var(--text); text-align: justify; }
  .chart-card { position: absolute; left: 77px; top: 257px; width: 296px; height: 187px; background: #fff; box-shadow: 0 0 10px rgba(0,0,0,0.07); }
  .chart-card svg { width: 100%; height: 100%; display: block; }
  .data-note { position: absolute; left: 77px; width: 296px; top: 462px; text-align: center; font-size: 6.7px; line-height: 14px; color: var(--text); }

  /* Back page */
  .back-band { position: absolute; left: 0; top: 333px; width: 301px; bottom: 0; background: var(--orange); }
  .back-photo { position: absolute; left: 36px; top: 30px; width: 337px; height: 401px;
    background: linear-gradient(160deg, #e9ebe4 0%, #cfd3c9 35%, #6f8f86 55%, #2f3640 80%, #d8d8d4 100%);
    box-shadow: 0 4px 12px rgba(0,0,0,0.15); }
  .credits { position: absolute; left: 36px; top: 447px; color: #fff; }
  .credits-label { font-size: 9.5px; font-weight: 700; letter-spacing: 0.02em; }
  .credits-list { list-style: none; margin-top: 2px; padding-left: 17px; font-size: 8.3px; line-height: 16.5px; }
</style>
</head>
<body>

  <section class="page page--cover">
    <div class="cover-frame"></div>
    <p class="cover-tagline">PROTECTING WHAT MATTERS MOST WITH RELIABLE INSURANCE SOLUTIONS</p>
    <h1 class="cover-title">HARWICK<br>ASSOCIATION<br>INSURANCE</h1>
    <p class="cover-lead">Comprehensive coverage for individuals, families, and businesses—tailored to your unique needs</p>
    <p class="cover-body">Nemo enim ipsam voluptatem quia voluptas sit aspernatur aut odit aut fugit, sed quia consequuntur magni dolores eos qui ratione voluptatem sequi nesciunt. Neque porro quisquam est, qui dolorem ipsum quia dolor sit amet, consectetur</p>
    <div class="date-pill">
      <svg width="7" height="7" viewBox="0 0 10 10" aria-hidden="true"><rect x="0.7" y="1.7" width="8.6" height="7.6" rx="1" fill="none" stroke="#fff" stroke-width="1"/><line x1="0.7" y1="4" x2="9.3" y2="4" stroke="#fff"/><line x1="3" y1="0.5" x2="3" y2="2.5" stroke="#fff"/><line x1="7" y1="0.5" x2="7" y2="2.5" stroke="#fff"/></svg>
      <span>03/01/2025</span>
    </div>
    <div class="cover-art" role="img" aria-label="Watercolour illustration of a row of colourful townhouses with trees and a street lamp"></div>
  </section>

  <section class="page page--data">
    <h2 class="data-title">INSURANCE SOLUTIONS FOR<br>EVERY NEED</h2>
    <div class="side-band"></div>
    <p class="data-kicker">WHETHER YOU'RE PROTECTING YOUR HOME, VEHICLE, OR BUSINESS, WE'VE GOT YOU COVERED.</p>
    <p class="data-body">Nemo enim ipsam voluptatem quia voluptas sit aspernatur aut odit aut fugit, sed quia consequuntur magni dolores eos qui ratione voluptatem sequi nesciunt. Neque porro quisquam est, qui dolorem ipsum quia dolor sit amet, consectetur, adipisci velit, sed quia non numquam eius modi tempora incidunt ut labore et dolore magnam aliquam quaerat voluptatem. Ut enim ad minima veniam, quis nostrum exercitationem ullam corporis suscipit laboriosam, nisi ut aliquid ex ea commodi consequatur? Quis autem vel eum iure reprehenderit qui in ea voluptate velit esse quam nihil molestiae consequatur, vel illum qui dolorem eum fugiat quo voluptas nulla pariatur</p>

    <div class="chart-card">
      <svg viewBox="0 0 532 335" aria-label="Monthly line chart comparing Lorem and Ipsum">
        <g font-family="Poppins, sans-serif" fill="#8a8f96">
          <text x="63" y="30" font-size="12">Line Chart</text>
          <text x="63" y="42" font-size="7">Editable values. Monthly trend lines.</text>
        </g>
        <line x1="63" y1="32" x2="496" y2="32" stroke="#c9ccd0" stroke-width="1"/>
        <g stroke="var(--grid)" stroke-width="1">
          <line x1="63" y1="63" x2="496" y2="63"/><line x1="63" y1="82" x2="496" y2="82"/>
          <line x1="63" y1="101" x2="496" y2="101"/><line x1="63" y1="120" x2="496" y2="120"/>
          <line x1="63" y1="139" x2="496" y2="139"/><line x1="63" y1="158" x2="496" y2="158"/>
          <line x1="63" y1="177" x2="496" y2="177"/><line x1="63" y1="197" x2="496" y2="197"/>
          <line x1="63" y1="216" x2="496" y2="216"/><line x1="63" y1="235" x2="496" y2="235"/>
          <line x1="63" y1="254" x2="496" y2="254" stroke="#aab0b6"/>
          <line x1="63" y1="63" x2="63" y2="254"/><line x1="99" y1="63" x2="99" y2="254"/>
          <line x1="135" y1="63" x2="135" y2="254"/><line x1="171" y1="63" x2="171" y2="254"/>
          <line x1="207" y1="63" x2="207" y2="254"/><line x1="243" y1="63" x2="243" y2="254"/>
          <line x1="279" y1="63" x2="279" y2="254"/><line x1="315" y1="63" x2="315" y2="254"/>
          <line x1="351" y1="63" x2="351" y2="254"/><line x1="387" y1="63" x2="387" y2="254"/>
          <line x1="423" y1="63" x2="423" y2="254"/><line x1="459" y1="63" x2="459" y2="254"/>
          <line x1="496" y1="63" x2="496" y2="254"/>
        </g>
        <g font-family="Poppins, sans-serif" font-size="9" fill="#7d838a" text-anchor="end">
          <text x="56" y="66">100%</text><text x="56" y="85">90%</text><text x="56" y="104">80%</text>
          <text x="56" y="123">70%</text><text x="56" y="142">60%</text><text x="56" y="161">50%</text>
          <text x="56" y="180">40%</text><text x="56" y="200">30%</text><text x="56" y="219">20%</text>
          <text x="56" y="238">10%</text>
        </g>
        <g font-family="Poppins, sans-serif" font-size="9" fill="#7d838a" text-anchor="middle">
          <text x="81" y="271">Jan</text><text x="117" y="271">Feb</text><text x="153" y="271">Mar</text>
          <text x="189" y="271">Apr</text><text x="225" y="271">May</text><text x="261" y="271">Jun</text>
          <text x="297" y="271">Jul</text><text x="333" y="271">Aug</text><text x="369" y="271">Sep</text>
          <text x="405" y="271">Oct</text><text x="441" y="271">Nov</text><text x="478" y="271">Dec</text>
        </g>
        <polyline fill="none" stroke="var(--blue)" stroke-width="1.6" points="63,244 99,197 135,225 171,187 207,92 243,126 279,113 315,168 351,168 387,172 423,153 459,95 496,130"/>
        <polyline fill="none" stroke="var(--pink)" stroke-width="1.6" points="63,168 99,130 135,189 171,225 207,208 243,168 279,76 315,130 351,204 387,187 423,130 459,130 496,172"/>
        <g fill="var(--blue)">
          <circle cx="63" cy="244" r="2.6"/><circle cx="99" cy="197" r="2.6"/><circle cx="135" cy="225" r="2.6"/><circle cx="171" cy="187" r="2.6"/><circle cx="207" cy="92" r="2.6"/><circle cx="243" cy="126" r="2.6"/><circle cx="279" cy="113" r="2.6"/><circle cx="315" cy="168" r="2.6"/><circle cx="351" cy="168" r="2.6"/><circle cx="387" cy="172" r="2.6"/><circle cx="423" cy="153" r="2.6"/><circle cx="459" cy="95" r="2.6"/><circle cx="496" cy="130" r="2.6"/>
        </g>
        <g fill="var(--pink)">
          <circle cx="63" cy="168" r="2.6"/><circle cx="99" cy="130" r="2.6"/><circle cx="135" cy="189" r="2.6"/><circle cx="171" cy="225" r="2.6"/><circle cx="207" cy="208" r="2.6"/><circle cx="243" cy="168" r="2.6"/><circle cx="279" cy="76" r="2.6"/><circle cx="315" cy="130" r="2.6"/><circle cx="351" cy="204" r="2.6"/><circle cx="387" cy="187" r="2.6"/><circle cx="423" cy="130" r="2.6"/><circle cx="459" cy="130" r="2.6"/><circle cx="496" cy="172" r="2.6"/>
        </g>
        <g font-family="Poppins, sans-serif" font-size="9" fill="#7d838a">
          <circle cx="83" cy="302" r="2.6" fill="var(--blue)"/><text x="91" y="305">Lorem</text>
          <circle cx="155" cy="302" r="2.6" fill="var(--pink)"/><text x="163" y="305">Ipsum</text>
        </g>
      </svg>
    </div>

    <p class="data-note">Nemo enim ipsam voluptatem quia voluptas sit aspernatur aut odit aut fugit, sed quia consequuntur magni dolores eos qui ratione voluptatem sequi nesciunt. Neque porro quisquam est, qui dolorem ipsum quia dolor sit amet</p>
  </section>

  <section class="page page--back">
    <div class="back-band"></div>
    <div class="back-photo" role="img" aria-label="Photo of hands holding a small teal umbrella over a model house on a desk with contract papers and pens"></div>
    <div class="credits">
      <p class="credits-label">POWERED BY</p>
      <ul class="credits-list">
        <li>Daniel Moreno</li>
        <li>Quis autem vel eum iure reprehenderit</li>
        <li>03/01/2025</li>
      </ul>
    </div>
  </section>

</body>
</html>
```